Velvet Crest Car Detailing Brochure

I would like a trifold brochure designed for my car detailing business. The background has to be full black or mostly black with some designing using only colors present in our logo.

Front page must have our logo and name, list of services, a photo and mybe our phone number but no long text.

Inside I want to present each service one by one with its description and a photo representing/showing each service. (I will provide the text below). For photos, use stock photos and I will add come of mines already too.

On the back of the brochure I want to have contact & info: phone number, opening hours, address, website, Instagram.

Outside left I want the text About us and photo/design.

I want the brochure to be neat, professional, easy to read, but at the same time not too boring.

Text:
1. About us
a. the ultimate destination for car care in Geneva. We provide personalized, detail-oriented services that bring out the best in your car. With our expert techniques and dedicated approach, we ensure that your car receives the utmost care and attention. Experience a place where passion meets precision and let us create an exceptional car care experience designed just for you.
2. Services:

DETAILING & HAND WASH

• Comprehensive exterior & interior care
• Personalisation and tailored cleaning packages
• Decontamination
• Premium products
• Attention to detail for a perfect finish

POLISHING

• Eliminates scratches, holograms
• Revives and protects paint
• Ensures lasting gloss
• Enhances paint life
• Preserves car’s value and beauty

CERAMIC TREATMENT

• Durable paint protection
• Water-repellent (hydrophobic) effect
• Easier cleaning, enhanced shine
• Long-term surface safeguarding
• Shields against environmental impacts

DRY ICE WASH

• Innovative, waterless method
• Safe for all car parts
• Deep cleans, removes odors
• Allergen-free, antibacterial
• Gentle, effective
• Advanced cleaning technology

COVERING

• Personalized vehicle styling
• More than 150 colours available
• Clean cut without using a cutter
• High-quality, durable materials
• Custom designs available

PROTECTION FILM

• Invisible, durable shield
• Self-healing technology
• 10-year warranty by QR VONT

DETAILING BOUTIQUE

• Premium brands available
• Buy on site during your visit
• Marble Harbour, Zeb Autos, DRUP Polaro
• Essential for at-home car care
• Perfect for quick touch-ups
(for these three brands you can put their logos

Target Market(s)

Our target market includes car owners of all price ranges, with a special focus on those who are passionate about their vehicles. We cater to clients who value excellent service and results, and seek to maintain their cars in pristine condition.

Industry/Entity Type

Automobile / Car detailing

Colors

Designer to choose colors to be used in the design.

Requirements
Must have
• Brand Consistency: The brochure must adhere to our brand colors and style, particularly utilizing the colors present in our logo. Trifold Layout: The design must be specifically tailored for a trifold brochure format. Legibility: Text must be easy to read against the mostly black background, with appropriate font size and style. Professional Look and Feel: The overall design must convey professionalism while being engaging and not overly complex. Photo representation: each service description should have a phot presenting it.
Should not have
• Overcrowded Design: Avoid cluttering with too much text or too many images. The layout should be clean and easy to navigate. Cartoonish Fonts or Graphics: Avoid using unprofessional or casual fonts and graphics that do not align with the upscale and professional image of our business. Distracting Backgrounds: The background should complement and not overpower the content. Stick to the theme of mostly black with design elements from our logo.

```html
<!DOCTYPE html>
<html lang="en">
<head>
<meta charset="utf-8">
<title>Velvet Crest Car Detailing – Trifold Brochure</title>
<link rel="stylesheet" href="https://fonts.googleapis.com/css2?family=Montserrat:wght@300;400;500;600;700;800&display=swap">
<style>
  :root {
    --stage: #e3e3e7;
    --ink: #0d090d;
    --white: #ffffff;
    --blue: #3a8fdc;
    --purple: #8a5cc9;
    --pink: #d8369c;
    --rule: #4a4a4a;
    --brand-gradient: linear-gradient(90deg, var(--blue), var(--purple) 50%, var(--pink));
  }
  * { box-sizing: border-box; margin: 0; padding: 0; }
  html, body { width: 1200px; height: 1200px; overflow: hidden; }
  body {
    background: var(--stage);
    font-family: "Montserrat", sans-serif;
    color: var(--white);
    position: relative;
  }
  .panel {
    position: absolute;
    left: 247px;
    width: 707px;
    height: 500px;
    background: var(--ink);
    overflow: hidden;
  }
  .panel--outside { top: 60px; }
  .panel--inside { top: 610px; }
  .panel__art { position: absolute; inset: 0; width: 707px; height: 500px; }
  .abs { position: absolute; }

  /* ---------- outside ---------- */
  .offer-title {
    left: 30px; top: 33px;
    font-size: 28px; font-weight: 700; line-height: 26px; letter-spacing: 0.3px;
  }
  .offer-item {
    left: 61px;
    font-size: 15.5px; font-weight: 500; line-height: 15px; letter-spacing: 0.2px;
  }
  .offer-item::before {
    content: ""; position: absolute; left: -28px; top: 0;
    width: 15px; height: 15px; border-radius: 50%;
    background: linear-gradient(90deg, var(--blue), var(--pink));
  }
  .details-heading {
    left: 271px; top: 44px; width: 170px;
    font-size: 17.5px; font-weight: 800; line-height: 27px;
  }
  .contact {
    left: 274px; width: 160px; text-align: center;
    font-weight: 700;
  }
  .contact--title { top: 196px; font-size: 17.5px; font-weight: 800; letter-spacing: 0.3px; }
  .contact--line { font-size: 11.5px; line-height: 15px; }
  .brand-mark {
    left: 470px; top: 84px; width: 105px; text-align: center;
    font-size: 13.5px; font-weight: 300; line-height: 16px; letter-spacing: 0.5px;
  }
  .welcome {
    left: 518px; top: 424px;
    font-size: 21px; font-weight: 700; line-height: 27px;
  }

  /* ---------- inside ---------- */
  .section-title { font-size: 27px; line-height: 27px; }
  .section-title .light { font-weight: 400; display: block; }
  .section-title .bold {
    font-weight: 700; display: block;
    background: var(--brand-gradient); -webkit-background-clip: text; background-clip: text; color: transparent;
  }
  .section-title--services { right: 252px; top: 128px; text-align: right; }
  .section-title--services .light { color: var(--purple); }
  .section-title--company { left: 18px; top: 272px; font-size: 25px; line-height: 25px; }
  .section-title--company .light { color: var(--blue); }
  .company-text {
    left: 21px; top: 339px; width: 196px;
    font-size: 7.6px; line-height: 12px; font-weight: 400;
  }
  .service { position: absolute; }
  .service::before {
    content: ""; position: absolute; left: -27px; top: -3px;
    width: 21px; height: 21px; border-radius: 50%;
    background: linear-gradient(90deg, var(--blue), var(--pink));
  }
  .service__name { font-size: 12.4px; font-weight: 600; line-height: 15px; letter-spacing: 0.2px; }
  .service__list { list-style: none; margin-top: 0; }
  .service__list li { font-size: 7.6px; line-height: 12px; padding-left: 4px; }
  .service__list li::before { content: "· "; }
  .boutique {
    left: 520px; top: 253px; width: 120px; text-align: center;
  }
  .boutique__title {
    font-size: 21px; font-weight: 800; line-height: 22px;
    background: var(--brand-gradient); -webkit-background-clip: text; background-clip: text; color: transparent;
  }
  .boutique__sub { font-size: 12px; font-weight: 400; line-height: 14px; }
  .partner-row { display: flex; justify-content: center; gap: 8px; margin-top: 7px; }
  .partner { font-size: 8.5px; font-weight: 700; line-height: 11px; text-transform: uppercase; }
</style>
</head>
<body>

<!-- Outside spread -->
<section class="panel panel--outside">
  <svg class="panel__art" viewBox="0 0 1138 805" preserveAspectRatio="none">
    <defs>
      <linearGradient id="outTop" x1="0" y1="0" x2="1" y2="0">
        <stop offset="0" stop-color="#5c63d0"/>
        <stop offset="0.5" stop-color="#8a5cc9"/>
        <stop offset="1" stop-color="#d8369c"/>
      </linearGradient>
      <linearGradient id="outBottom" x1="0" y1="0" x2="1" y2="0">
        <stop offset="0" stop-color="#3a8fdc"/>
        <stop offset="0.5" stop-color="#8a5cc9"/>
        <stop offset="1" stop-color="#d8369c"/>
      </linearGradient>
      <linearGradient id="outPhoto" x1="0" y1="0" x2="1" y2="1">
        <stop offset="0" stop-color="#d9d9d6"/>
        <stop offset="0.6" stop-color="#a9a9a6"/>
        <stop offset="1" stop-color="#6e6e70"/>
      </linearGradient>
      <linearGradient id="outCircle" x1="0" y1="0" x2="1" y2="1">
        <stop offset="0" stop-color="#9fa3a8"/>
        <stop offset="1" stop-color="#4c4f55"/>
      </linearGradient>
    </defs>
    <path role="img" aria-label="Photo: hand cleaning a white car's wheel with a foam brush"
          d="M760 274 C900 272 1040 245 1138 215 L1138 520 C1030 590 900 630 760 645 Z" fill="url(#outPhoto)"/>
    <path d="M1138 95 C1000 200 850 255 690 262 C870 264 1020 222 1138 158 Z" fill="url(#outTop)"/>
    <path d="M218 0 C330 160 480 250 700 262" fill="none" stroke="#3a8fdc" stroke-width="2"/>
    <path d="M0 552 C100 600 200 622 323 616" fill="none" stroke="#3a8fdc" stroke-width="2"/>
    <path d="M323 616 C520 682 820 680 1138 522 L1138 592 C900 662 600 702 323 616 Z" fill="url(#outBottom)"/>
    <path d="M298 689 C420 722 620 716 800 652" fill="none" stroke="url(#outBottom)" stroke-width="2.5"/>
    <circle role="img" aria-label="Photo: foam wash on a grey sports car bonnet" cx="191" cy="614" r="130" fill="url(#outCircle)"/>
    <line x1="376" y1="132" x2="376" y2="629" stroke="#4a4a4a" stroke-width="1.5"/>
    <rect x="522" y="53" width="91" height="6" fill="url(#outBottom)"/>
    <rect x="522" y="173" width="91" height="6" fill="url(#outBottom)"/>
    <circle cx="841" cy="72" r="50" fill="none" stroke="#d8369c" stroke-width="3"/>
  </svg>

  <h2 class="abs offer-title">SERVICES<br>WE<br>OFFERS</h2>
  <div class="abs offer-item" style="top:123px">DETAILING &amp;<br>HAND WASH</div>
  <div class="abs offer-item" style="top:157px">POLISHING</div>
  <div class="abs offer-item" style="top:179px">CERAMIC<br>TREATMENT</div>
  <div class="abs offer-item" style="top:215px">DRY ICE WASH</div>
  <div class="abs offer-item" style="top:240px">COVERING</div>
  <div class="abs offer-item" style="top:269px">PROTECTION FILM</div>

  <h2 class="abs details-heading">YOUR COMPANY DETAILS HERE</h2>

  <div class="abs contact contact--title">CONTACT US</div>
  <div class="abs contact contact--line" style="top:234px">+00 000 000000<br>+00 000 000000</div>
  <div class="abs contact contact--line" style="top:283px">@YOURCOMPANY</div>
  <div class="abs contact contact--line" style="top:318px">@YOURCOMPANY</div>

  <div class="abs brand-mark">VELVET<br>CREST</div>

  <h1 class="abs welcome">Welcome to<br>Velvet Crest</h1>
</section>

<!-- Inside spread -->
<section class="panel panel--inside">
  <svg class="panel__art" viewBox="0 0 1138 805" preserveAspectRatio="none">
    <defs>
      <linearGradient id="inBand" x1="0" y1="0" x2="1" y2="0">
        <stop offset="0" stop-color="#3a8fdc"/>
        <stop offset="0.5" stop-color="#8a5cc9"/>
        <stop offset="1" stop-color="#d8369c"/>
      </linearGradient>
      <linearGradient id="inPhoto" x1="0" y1="0" x2="1" y2="1">
        <stop offset="0" stop-color="#5c6466"/>
        <stop offset="0.5" stop-color="#34383b"/>
        <stop offset="1" stop-color="#1c1e22"/>
      </linearGradient>
      <linearGradient id="inCircle" x1="0" y1="0" x2="1" y2="1">
        <stop offset="0" stop-color="#6a6d72"/>
        <stop offset="0.55" stop-color="#c7782e"/>
        <stop offset="1" stop-color="#2a2b2e"/>
      </linearGradient>
    </defs>
    <path role="img" aria-label="Photo: rotary polisher buffing a black car panel"
          d="M0 0 L675 0 C560 200 300 310 0 328 Z" fill="url(#inPhoto)"/>
    <path d="M0 330 C300 312 560 200 675 0 L690 0 C600 222 330 372 0 390 Z" fill="url(#inBand)"/>
    <path d="M0 410 C340 392 620 232 700 0" fill="none" stroke="url(#inBand)" stroke-width="2"/>
    <path d="M640 805 C780 662 960 610 1138 612 L1138 805 Z" fill="url(#inBand)"/>
    <circle role="img" aria-label="Photo: orange microfibre towel and care product on carbon fibre" cx="960" cy="658" r="120" fill="url(#inCircle)"/>
  </svg>

  <h2 class="abs section-title section-title--services"><span class="light">OUR</span><span class="bold">SERVICES</span></h2>

  <h2 class="abs section-title section-title--company"><span class="light">OUR</span><span class="bold">COMPANY</span></h2>
  <p class="abs company-text">Your Company Details here.....Your Company Details here.....Your Company Details here.....Your Company Details here.....Your Company Details here.....Your Company Details here.....Your Company Details here.....Your Company Details here.....Your Company Details here.....Your Company Details here.....Your Company Details here.....Your Company Details here.....Your Company Details here.....Your Company Details here.....Your Company Details here.....Your Company Details here.....Your Company Details here.....Your Company Details here.....Your Company Details here.....</p>

  <article class="service" style="left:283px; top:214px">
    <h3 class="service__name">DETAILING &amp; HAND WASH</h3>
    <ul class="service__list">
      <li>Comprehensive exterior &amp; interior care</li>
      <li>Personalisation and tailored cleaning packages</li>
      <li>Decontamination</li>
      <li>Premium products</li>
      <li>Attention to detail for a perfect finish</li>
    </ul>
  </article>

  <article class="service" style="left:283px; top:295px">
    <h3 class="service__name">POLISHING</h3>
    <ul class="service__list">
      <li>Eliminates scratches, holograms</li>
      <li>Revives and protects paint</li>
      <li>Ensures lasting gloss</li>
      <li>Enhances paint life</li>
      <li>Preserves car’s value and beauty</li>
    </ul>
  </article>

  <article class="service" style="left:285px; top:378px">
    <h3 class="service__name">COVERING</h3>
    <ul class="service__list">
      <li>Personalized vehicle styling</li>
      <li>More than 150 colours available</li>
      <li>Clean cut without using a cutter</li>
      <li>High-quality, durable materials</li>
      <li>Custom designs available</li>
    </ul>
  </article>

  <article class="service" style="left:520px; top:18px">
    <h3 class="service__name">CERAMIC TREATMENT</h3>
    <ul class="service__list">
      <li>Durable paint protection</li>
      <li>Water-repellent (hydrophobic) effect</li>
      <li>Easier cleaning, enhanced shine</li>
      <li>Long-term surface safeguarding</li>
      <li>Shields against environmental impacts</li>
    </ul>
  </article>

  <article class="service" style="left:520px; top:99px">
    <h3 class="service__name">DRY ICE WASH</h3>
    <ul class="service__list">
      <li>Innovative, waterless method</li>
      <li>Safe for all car parts</li>
      <li>Deep cleans, removes odors</li>
      <li>Allergen-free, antibacterial</li>
      <li>Gentle, effective</li>
      <li>Advanced cleaning technology</li>
    </ul>
  </article>

  <article class="service" style="left:518px; top:194px">
    <h3 class="service__name">PROTECTION FILM</h3>
    <ul class="service__list">
      <li>Invisible, durable shield</li>
      <li>Self-healing technology</li>
      <li>10-year warranty by QR VONT</li>
    </ul>
  </article>

  <div class="abs boutique">
    <div class="boutique__title">BOUTIQUE</div>
    <div class="boutique__sub">Buy Products</div>
    <div class="partner-row">
      <span class="partner">Marble Harbour</span>
      <span class="partner">DRUP Polaro</span>
    </div>
    <div class="partner-row" style="margin-top:3px">
      <span class="partner">Zeb Autos</span>
    </div>
  </div>
</section>

</body>
</html>
```